Vendro Sahel - Website Design Brief

Web Design Brief

VENDRO SAHEL
WEBSITE DESIGN BRIEF

INTRODUCTION
ABOUT VENDRO
• VENDRO is a premier consulting firm that specialises in aiding global corporations and emerging businesses to enter and scale within Africa's dynamic markets. Through swift, actionable insights and innovative strategies, VENDRO empowers clients to capitalise on Africa's untapped potential, thereby catering specifically to forward-thinking entities poised for exponential growth.

TASK DESCRIPTION
• Develop a 5-page website for VENDRO.
• The primary goal is to present a clear and concise picture of our consulting firm, its Africa-centric experience, and its offerings to multinational clients looking for a professional partner to penetrate African markets or reclaim lost market share.

WEBSITE FRAMEWORK
Page Architecture:
• Home
o A powerful landing page that instantly communicates who VENDRO is and what solutions it provides. Incorporate impactful visuals and calls-to-action.
• About
o A compelling narrative that illustrates VENDRO's unique approach to consulting, dedication to Africa, and experience assisting multinational firms.
• Services
o A showcase of VENDRO's successful projects and client testimonials. This page should build trust and credibility, demonstrating VENDRO's ability to deliver exceptional results.
• Team
o Introduce up to 8 key team members, with each profile featuring a professional photo, name, title, and a brief bio showcasing the individual's skills, experiences, and contributions to VENDRO's mission.
• Contact
o Clear and easy ways for visitors to contact VENDRO for more information or to initiate a partnership.
• Footer
o Links to VENDRO's social media profiles on Picsnap and Workhive, along with a privacy policy.
o Social links
o Picsnap: https://www.instagram.com/vendrosahel/
o Workhive: https://www.linkedin.com/company/vendrosahel/
o Privacy Policy
o Insert placeholder "lorem ipsum" text.
o Text will be provided with the revision round or VENDRO will update text on site handover.

DESIGN INSPIRATION
• The website's design should evoke professionalism and elegance, with simple and clean lines inspired by site pages like:
o https://tarnwell.example/
o https://tarnwell.example/services/
o One aspect we particularly appreciate is how visitors can easily navigate by scrolling down to find what they're looking for and see everything they need to in an intuitive way on the home page
o What we don’t like about this site is how they navigate from the home page to other random pages – we like about to take you to the about page, and so on.

Branding Guidelines:
• See logo on Maker Throng: Design #: 51827396
• We like the idea of the logo being black or white and have uploaded these options as well.
• Monochrome themes, with spots or splash of colour to highlight something is a style we appreciate.

Website Objectives and Goals:
• Our website's primary goal is to create a strong online presence, acting as a hub for potential clients to discover our credibility, reliability, and our ability to deliver exceptional results. It's essential that our website portrays professionalism, instils trustworthiness, and showcases our sincere dedication to Africa.

Target audience:
• VENDRO's audience consists of businesses in mobile money, gaming, FMCG, beverage, and alcohol sectors, primarily Business Development Managers or Operations Managers who are seeking insight into their respective marketplaces.

Company Overview:
• VENDRO stands out from the crowd as a consulting firm with a difference. Our dynamic team is fully dedicated to one mission: brand development within Africa.
• Unlike other companies that focus solely on online connectivity, we recognize the tremendous value in embracing the vibrant street culture that makes Africa so unique. Community engagement, empowerment, and expansion are at the forefront of everything we do.
• we recognize that unlocking business growth starts with a deep understanding of consumer behavior. It is this understanding that bridges the gap between companies and the communities that drive the cash economy. Our purpose is to reconnect businesses with the vibrant pulse of these essential local markets, injecting fresh vitality into their brands and propelling them towards resounding success in Africa.

Development to include:
• Basic SEO Setup:
o The website should be optimized for search engines, incorporating keywords, meta tags, and alt tags for images.
• Searchly Metrics Setup.
o To track website traffic and user behaviour for ongoing optimization.
• Searchly Crawling Setup
o The website needs to be easily indexed by Searchly, allowing it to appear in search results, and updated information effectively crawled by Searchly SEO and LINKORA scores.

PAGE CONTENT:
Home Page
• Background
o Option #1
o 4K video on home page, running on loop
o Bold Statement Text over Video
o Option #2
o Still Image
o Animated text making bold statement (e.g. our motto)

• Sections
o Contrast colour blocks or a way of making it clear that the next topic is a new topic.
o 5 sections
1. Home Main - Video + bold statement text
2. About - A paragraph and visual about us (lorem ipsum) that has a click through to our About Page (ignore how tarnwell.example navigate, we think this is too complicated for our needs)
3. Services – communicated in some simple and powerful ways (we leave this open to you) – but keeping in mind it needs to be concise and professional.
4. Other - Something about our process that makes us unique (lorem ipsum text) and a placeholder image/animation.
5. Contact – a call-to-action button that takes you to our contact, but showcases a mobile number and email address.
6. Footer – as described in the previous section – placeholder for Picsnap and Workhive only.

About Page
• Don’t reference tarnwell.example for this page.
• Main Section
o Bold statements and images
• History Section
o A story about us and our past
• Final Section
o Some of our comments and final thoughts

Services Page
• How https://tarnwell.example/services/ is laid out is great – we prefer a light theme.
• 6 - 8 x icons with headings and a brief description text box, and a read more drop down – all as placeholders to be edited later.
• For ease of direction for this page, look to the link shared above.

Team
• Add Placeholders for up to 8 team members (we only have 4 now):
o Image placeholder
o Name placeholder
o Title placeholder
o Short Bio (lorem ipsum)

Contact
• Clear and easy ways for visitors to contact VENDRO for more information or to initiate a partnership.

• Insert placeholder "lorem ipsum" text, we will provide the text with our revision round.
o Ideally an easy form process that gives the user some options or dropdowns to complete before submission – up to 3 would be sufficient.
o Require their name and contact details.

NOTE: Images to follow:

Target Market(s)

VENDRO's audience consists of businesses in mobile money, gaming, FMCG, beverage, and alcohol sectors, primarily Business Development Managers or Operations Managers who are seeking insight into their respective marketplaces.

Industry/Entity Type

VENDRO is a premier consulting firm that specialises in aiding global corporations and emerging businesses to enter and scale within Africa's dynamic markets

Coding

Coded - Design and coding required

Number of Pages Required

5+ page

Font styles to use
Sans Serif
Other font styles liked:
• Poppins Font Family

Colors

Designer to choose colors to be used in the design.

Requirements
Must have
• The primary goal is to present a clear and concise picture of our consulting firm, and it's specialisation in Africa - smooth and crisp UI with animations or transitions that imply we know our way around tecchnology is always helpful - but a Clean and responsive UI is most important.
Nice to have
• Reactive and animated transitions through sections or pages - not overdone - adds a professional feel to the site
Should not have
• We don't want too many colours, and we don't want it too dark - we want a monochrome theme, with accents of colour when relevant

```html
<!DOCTYPE html>
<html lang="en">
<head>
<meta charset="utf-8">
<title>VENDRO – Home</title>
<link href="https://fonts.googleapis.com/css2?family=Montserrat:wght@600;700;800&family=Roboto:wght@400;500;700&display=swap" rel="stylesheet">
<style>
:root{
  --black:#000;
  --panel:#111214;
  --touch:#1b1e23;
  --bar:#1a1a1a;
  --white:#fff;
  --muted:#cfd2d6;
  --accent:#0a6fd1;
  --accent-dark:#075cae;
  --line:#9aa0a6;
}
*{box-sizing:border-box;margin:0;padding:0}
html,body{width:1200px;height:3144px;overflow:hidden;background:var(--black);color:var(--white);font-family:'Roboto',sans-serif}
.page{position:relative;width:1200px;height:3144px}
.abs{position:absolute}
section,header,footer{position:absolute;left:0;width:1200px}
.display{font-family:'Montserrat',sans-serif;font-weight:800;letter-spacing:-0.5px}

/* header */
.site-header{top:0;height:138px;background:var(--black)}
.brand{display:flex;align-items:center;gap:12px;font-family:'Montserrat',sans-serif;font-weight:600;color:var(--white);letter-spacing:1px}
.brand-mark{border:5px solid var(--white)}
.header-brand{left:112px;top:36px;font-size:50px}
.header-brand .brand-mark{width:56px;height:56px}
.contact-chip{display:flex;align-items:center;gap:10px}
.chip-icon{width:44px;height:44px;border-radius:50%;background:var(--white);display:flex;align-items:center;justify-content:center}
.chip-label{font-size:12px;font-weight:700}
.chip-value{font-size:15.5px;font-weight:700;margin-top:3px}
.quote-btn{left:958px;top:31px;width:130px;height:40px;background:var(--white);color:#111;font-size:15px;font-weight:500;display:flex;align-items:center;justify-content:center}
.main-nav{right:111px;top:98px;display:flex;gap:38px;font-size:15px;font-weight:500;text-transform:uppercase}
.main-nav span.sep{font-weight:400}

/* hero */
.hero{top:138px;height:601px;background:linear-gradient(160deg,#7b6d5e 0%,#8b8577 30%,#6f6b5f 55%,#556049 75%,#7c6c58 100%)}
.hero-shade{position:absolute;inset:0;background:rgba(0,0,0,.32)}
.hero-title{top:180px;width:100%;text-align:center;font-size:64px;text-shadow:0 2px 6px rgba(0,0,0,.35)}
.hero-copy{top:268px;width:100%;text-align:center;font-size:16.5px;line-height:27px;font-weight:500;text-shadow:0 1px 3px rgba(0,0,0,.6)}
.btn{display:flex;align-items:center;justify-content:center;gap:10px;font-size:16px;font-weight:700;text-transform:uppercase}
.btn-light{background:var(--white);color:#111}
.btn-accent{background:var(--accent);color:var(--white)}
.hero-btn{left:510px;top:349px;width:181px;height:51px}
.slide-arrow{top:277px;width:40px;height:40px;border-radius:50%;background:rgba(0,0,0,.65);display:flex;align-items:center;justify-content:center}

/* about */
.about{top:739px;height:594px;background:var(--black)}
.section-title{font-size:34px}
.about-title{left:112px;top:104px;display:flex;align-items:center;gap:14px}
.about-title::after{content:"";width:58px;height:4px;background:var(--accent)}
.about-copy{left:112px;top:160px;width:448px;font-size:14.5px;line-height:26.5px;text-align:justify}
.about-copy p+p{margin-top:14px}
.about-btn{left:113px;top:432px;width:156px;height:48px;font-size:15px}
.about-frame{left:657px;top:91px;width:432px;height:399px;border:1.5px solid #ddd}
.about-photo{left:647px;top:102px;width:431px;height:397px;background:linear-gradient(150deg,#c03a2e 0%,#8a7a6a 25%,#4f7a55 45%,#b9b2a8 65%,#6e5a4c 100%)}

/* process */
.process{top:1333px;height:437px;background:var(--panel)}
.center-title{width:100%;text-align:center}
.underline{left:572px;width:58px;height:4px;background:var(--accent)}
.step{top:160px;width:260px;text-align:center}
.step svg{display:block;margin:0 auto}
.step p{margin-top:18px;font-size:16px;line-height:25px}

/* services */
.services{top:1770px;height:611px;background:var(--black)}
.svc{width:340px}
.svc h3{font-size:19px;font-weight:700}
.svc p{font-size:13.5px;line-height:18px;margin-top:6px}
.svc-left{left:-24px;text-align:right}
.svc-right{left:891px}
.svc-icon{width:78px;height:78px;background:var(--accent);border:2px solid #6fb1f2;box-shadow:inset 0 0 0 4px var(--accent),inset 0 0 0 5px #cfe4fa;display:flex;align-items:center;justify-content:center}
.svc-photo{left:442px;top:189px;width:327px;height:331px;background:linear-gradient(135deg,#8d8d8d 0%,#5d5d5d 40%,#9a9a9a 70%,#4a4a4a 100%)}

/* touch */
.touch{top:2381px;height:366px;background:linear-gradient(180deg,#1d2127,#15181c)}
.field{top:158px;width:440px;height:50px;border:1.5px solid #c9ccd0;display:flex;align-items:center;padding-left:17px;font-size:14px;color:#c4c7cb}
.touch-btn{left:510px;top:247px;width:181px;height:52px}

/* footer */
.site-footer{top:2747px;height:339px;background:var(--black)}
.footer-brand{left:112px;top:76px;font-size:36px;gap:9px}
.footer-brand .brand-mark{width:40px;height:40px;border-width:4px}
.col-title{font-size:18px;font-weight:700;text-transform:uppercase}
.col-title::after{content:"";display:block;width:64px;height:3px;background:var(--accent);margin-top:8px}
.links{list-style:none;font-size:15.5px;line-height:31px;margin-top:17px}
.contact-row{display:flex;align-items:flex-start;gap:12px;font-size:15.5px;line-height:20px}
.dot-icon{width:24px;height:24px;border-radius:50%;background:#1e2430;display:flex;align-items:center;justify-content:center;flex:none}
.sub-copy{font-size:11.5px;line-height:20px;margin-top:18px}
.sub-field{margin-top:14px;width:252px;height:36px;border-radius:18px;background:#1c2028;display:flex;align-items:center;justify-content:space-between;overflow:hidden;font-size:10px;color:#9ba1a9;padding-left:14px}
.sub-send{width:48px;height:36px;background:var(--accent);border-radius:0 18px 18px 0;display:flex;align-items:center;justify-content:center}
.social{display:flex;gap:14px;margin-top:14px}
.social span{width:26px;height:26px;border-radius:50%;background:#1c1f25;display:flex;align-items:center;justify-content:center;font-size:10px;font-weight:700}
.chat-bubble{left:1121px;top:291px;width:36px;height:36px;border-radius:50%;background:#2a8ff0;display:flex;align-items:center;justify-content:center}

.bottom-bar{position:absolute;top:3086px;left:0;width:1200px;height:58px;background:var(--bar);font-size:14px;display:flex;align-items:center;justify-content:space-between;padding:0 111px 0 108px}
.bottom-bar u{font-weight:500}
</style>
</head>
<body>
<div class="page">

<header class="site-header">
  <div class="abs brand header-brand"><span class="brand-mark"></span>VENDRO</div>
  <div class="abs contact-chip" style="left:593px;top:31px">
    <span class="chip-icon"><svg width="22" height="22" viewBox="0 0 24 24"><path d="M6.6 10.8a15 15 0 0 0 6.6 6.6l2.2-2.2a1 1 0 0 1 1-.25 11.4 11.4 0 0 0 3.6.57 1 1 0 0 1 1 1V20a1 1 0 0 1-1 1A17 17 0 0 1 3 4a1 1 0 0 1 1-1h3.5a1 1 0 0 1 1 1c0 1.25.2 2.45.57 3.57a1 1 0 0 1-.25 1z" fill="#111"/></svg></span>
    <div><div class="chip-label">Phone:</div><div class="chip-value">+1 555 010 2040</div></div>
  </div>
  <div class="abs contact-chip" style="left:773px;top:31px">
    <span class="chip-icon"><svg width="24" height="24" viewBox="0 0 24 24" fill="none" stroke="#111" stroke-width="1.8"><rect x="3" y="6" width="18" height="12" rx="1.5"/><path d="M3 7l9 6 9-6"/></svg></span>
    <div><div class="chip-label">Email Address</div><div class="chip-value">info@vendro.com</div></div>
  </div>
  <div class="abs quote-btn">Get A Quote</div>
  <nav class="abs main-nav">
    <span>Home</span><span class="sep">|</span><span>About Us</span><span class="sep">|</span><span>Services</span><span class="sep">|</span><span>Team</span><span class="sep">|</span><span>Contact Us</span>
  </nav>
</header>

<section class="hero" role="img" aria-label="Aerial view of a busy African city highway with minibuses and rooftops">
  <div class="hero-shade"></div>
  <h1 class="abs display hero-title">WELCOME TO VENDRO</h1>
  <p class="abs hero-copy">Lorem ipsum dolor sit amet, consectetur adipiscing elit, sed do eiusmod tempor incididunt ut<br>labore et dolore magna aliqua.&nbsp; minim veniam, quis nostrud exercitation ullamco.</p>
  <div class="abs btn btn-light hero-btn">Get Started
    <svg width="15" height="15" viewBox="0 0 16 16"><circle cx="8" cy="8" r="8" fill="#111"/><path d="M6.5 4.5L10 8l-3.5 3.5" stroke="#fff" stroke-width="2" fill="none"/></svg></div>
  <div class="abs slide-arrow" style="left:28px"><svg width="12" height="20" viewBox="0 0 12 20"><path d="M10 2L2 10l8 8" stroke="#fff" stroke-width="1.6" fill="none"/></svg></div>
  <div class="abs slide-arrow" style="left:1131px"><svg width="12" height="20" viewBox="0 0 12 20"><path d="M2 2l8 8-8 8" stroke="#fff" stroke-width="1.6" fill="none"/></svg></div>
</section>

<section class="about">
  <h2 class="abs display section-title about-title">ABOUT US</h2>
  <div class="abs about-copy">
    <p>Lorem ipsum dolor sit amet, consectetur adipiscing elit, sed do eiusmod tempor incididunt ut labore et dolore magna aliqua. Ut enim ad minim veniam, quis nostrud exercitation ullamco labori.</p>
    <p>Lorem ipsum dolor sit amet, consectetur adipiscing elit, sed do eiusmod tempor incididunt ut labore et dolore magna aliqua. Ut enim ad minim veniam, quis nostrud exercitation ullamco laboris nisi ut aliquip ex ea commodo consequat. Duis aute irure dolor in reprehenderit in voluptate velit esse cillum dolore eu fugiat.</p>
  </div>
  <div class="abs btn btn-accent about-btn">Learn More
    <svg width="14" height="14" viewBox="0 0 16 16"><circle cx="8" cy="8" r="8" fill="#fff"/><path d="M6.5 4.5L10 8l-3.5 3.5" stroke="#0a6fd1" stroke-width="2" fill="none"/></svg></div>
  <div class="abs about-frame"></div>
  <div class="abs about-photo" role="img" aria-label="Consultant showing a phone to traders at an open-air market"></div>
</section>

<section class="process">
  <h2 class="abs display section-title center-title" style="top:58px">OUR PROCESS</h2>
  <div class="abs underline" style="top:109px"></div>

  <div class="abs step" style="left:78px">
    <svg width="160" height="140" viewBox="0 0 160 140">
      <path d="M58 29 A68 68 0 1 1 58 111" fill="none" stroke="var(--accent)" stroke-width="4"/>
      <circle cx="92" cy="70" r="42" fill="#1c1c1e"/>
      <text x="20" y="100" font-family="Montserrat" font-weight="800" font-size="86" fill="none" stroke="var(--accent)" stroke-width="3.5">1</text>
      <g stroke="#fff" stroke-width="1.6" fill="none"><circle cx="86" cy="66" r="7"/><path d="M74 88c0-8 6-12 12-12s12 4 12 12"/><path d="M100 62v-8M105 62v-12M110 62v-16"/></g>
    </svg>
    <p>Lorem ipsum dolor sit amet<br>consectetur adipiscing</p>
  </div>
  <div class="abs step" style="left:339px">
    <svg width="160" height="140" viewBox="0 0 160 140">
      <path d="M58 29 A68 68 0 1 1 58 111" fill="none" stroke="var(--accent)" stroke-width="4"/>
      <circle cx="92" cy="70" r="42" fill="#1c1c1e"/>
      <text x="14" y="100" font-family="Montserrat" font-weight="800" font-size="86" fill="none" stroke="var(--accent)" stroke-width="3.5">2</text>
      <g stroke="#fff" stroke-width="1.6" fill="none"><circle cx="92" cy="70" r="6"/><circle cx="80" cy="56" r="4.5"/><circle cx="104" cy="56" r="4.5"/><circle cx="80" cy="84" r="4.5"/><circle cx="104" cy="84" r="4.5"/><path d="M84 60l4 5M100 60l-4 5M84 80l4-5M100 80l-4-5"/></g>
    </svg>
    <p>Lorem ipsum dolor sit amet<br>consectetur adipiscing</p>
  </div>
  <div class="abs step" style="left:599px">
    <svg width="160" height="140" viewBox="0 0 160 140">
      <path d="M58 29 A64 64 0 1 1 58 111" fill="none" stroke="var(--accent)" stroke-width="4"/>
      <text x="20" y="100" font-family="Montserrat" font-weight="800" font-size="80" fill="none" stroke="var(--accent)" stroke-width="3.5">3</text>
      <g stroke="#fff" stroke-width="1.6" fill="none"><rect x="80" y="50" width="22" height="14" rx="2"/><circle cx="108" cy="58" r="4"/><path d="M84 55h14M84 59h10M102 72v16M96 72h18v16M78 88V70h12"/></g>
    </svg>
    <p>Lorem ipsum dolor sit amet<br>consectetur adipiscing</p>
  </div>
  <div class="abs step" style="left:859px">
    <svg width="160" height="140" viewBox="0 0 160 140">
      <path d="M58 29 A68 68 0 1 1 58 111" fill="none" stroke="var(--accent)" stroke-width="4"/>
      <circle cx="92" cy="70" r="42" fill="#1c1c1e"/>
      <text x="12" y="100" font-family="Montserrat" font-weight="800" font-size="86" fill="none" stroke="var(--accent)" stroke-width="3.5">4</text>
      <g stroke="#fff" stroke-width="1.6" fill="none"><circle cx="92" cy="56" r="7"/><path d="M92 63v4"/><circle cx="80" cy="74" r="4.5"/><circle cx="104" cy="74" r="4.5"/><path d="M72 90c0-6 4-9 8-9s8 3 8 9M96 90c0-6 4-9 8-9s8 3 8 9"/></g>
    </svg>
    <p>Lorem ipsum dolor sit amet<br>consectetur adipiscing</p>
  </div>
</section>

<section class="services">
  <h2 class="abs display section-title center-title" style="top:78px">OUR SERVICES</h2>
  <div class="abs underline" style="top:130px"></div>

  <div class="abs svc svc-left" style="top:192px"><h3>Identify Growth Pathways</h3><p>Lorem ipsum dolor sit&nbsp; consectetur<br>elit, sed do eiusmod tempor</p></div>
  <div class="abs svc svc-left" style="top:314px"><h3>Reimagine Brands</h3><p>Lorem ipsum dolor sit&nbsp; consectetur<br>elit, sed do eiusmod tempor</p></div>
  <div class="abs svc svc-left" style="top:436px"><h3>Revolutionize Experiences</h3><p>Lorem ipsum dolor sit&nbsp; consectetur<br>elit, sed do eiusmod tempor</p></div>

  <div class="abs svc-icon" style="left:338px;top:189px"><svg width="42" height="42" viewBox="0 0 42 42" fill="none" stroke="#fff" stroke-width="1.8"><path d="M21 4v14M15 10l6-6 6 6M9 10v8M5 14l4-4 4 4M33 10v8M29 14l4-4 4 4"/><circle cx="21" cy="26" r="4"/><path d="M13 38c0-5 4-7 8-7s8 2 8 7"/><circle cx="9" cy="28" r="3"/><circle cx="33" cy="28" r="3"/></svg></div>
  <div class="abs svc-icon" style="left:338px;top:311px"><svg width="44" height="44" viewBox="0 0 44 44" fill="none" stroke="#fff" stroke-width="1.8"><path d="M4 22c5-8 11-12 18-12s13 4 18 12c-5 8-11 12-18 12S9 30 4 22z"/><circle cx="22" cy="22" r="6"/><path d="M22 2v4M22 38v4M6 8l3 3M38 8l-3 3"/></svg></div>
  <div class="abs svc-icon" style="left:338px;top:433px"><svg width="44" height="44" viewBox="0 0 44 44" fill="none" stroke="#fff" stroke-width="1.8"><rect x="4" y="8" width="26" height="18" rx="1"/><path d="M13 32h8M17 26v6"/><rect x="26" y="18" width="10" height="18" rx="1.5"/><rect x="34" y="22" width="6" height="12" rx="1"/></svg></div>

  <div class="abs svc-photo" role="img" aria-label="People in an office corridor using phones and tablets"></div>

  <div class="abs svc-icon" style="left:793px;top:189px"><svg width="44" height="44" viewBox="0 0 44 44" fill="none" stroke="#fff" stroke-width="1.8"><circle cx="22" cy="22" r="16"/><path d="M28 10h10v8M14 34H6v-8"/><circle cx="22" cy="19" r="5"/><path d="M13 31c2-4 5-6 9-6s7 2 9 6"/></svg></div>
  <div class="abs svc-icon" style="left:793px;top:311px"><svg width="44" height="44" viewBox="0 0 44 44" fill="none" stroke="#fff" stroke-width="1.8"><circle cx="22" cy="9" r="5"/><path d="M14 24c0-5 4-8 8-8s8 3 8 8"/><path d="M4 18l6 12 8 4v6M40 18l-6 12-8 4v6"/></svg></div>
  <div class="abs svc-icon" style="left:793px;top:433px"><svg width="44" height="44" viewBox="0 0 44 44" fill="none" stroke="#fff" stroke-width="1.8"><circle cx="22" cy="22" r="18"/><circle cx="22" cy="18" r="4"/><circle cx="13" cy="21" r="3"/><circle cx="31" cy="21" r="3"/><path d="M14 32c0-5 4-8 8-8s8 3 8 8M7 30c0-3 2-5 6-5M37 30c0-3-2-5-6-5"/></svg></div>

  <div class="abs svc svc-right" style="top:192px"><h3>Drive Customer Demand</h3><p>Lorem ipsum dolor sit&nbsp; consectetur<br>elit, sed do eiusmod tempor</p></div>
  <div class="abs svc svc-right" style="top:314px"><h3>Empower Employees</h3><p>Lorem ipsum dolor sit&nbsp; consectetur<br>elit, sed do eiusmod tempor</p></div>
  <div class="abs svc svc-right" style="top:436px"><h3>Lorem ipsum dolor sit</h3><p>Lorem ipsum dolor sit&nbsp; consectetur<br>elit, sed do eiusmod tempor</p></div>
</section>

<section class="touch">
  <h2 class="abs display section-title center-title" style="top:59px">GET IN TOUCH</h2>
  <div class="abs underline" style="top:114px;background:var(--white)"></div>
  <div class="abs field" style="left:151px">Mobile number:</div>
  <div class="abs field" style="left:608px;padding-left:25px">Email:</div>
  <div class="abs btn btn-accent touch-btn">Submit Now
    <svg width="15" height="15" viewBox="0 0 16 16"><circle cx="8" cy="8" r="8" fill="#fff"/><path d="M6.5 4.5L10 8l-3.5 3.5" stroke="#0a6fd1" stroke-width="2" fill="none"/></svg></div>
</section>

<footer class="site-footer">
  <div class="abs brand footer-brand"><span class="brand-mark"></span>VENDRO</div>

  <div class="abs" style="left:351px;top:83px">
    <h4 class="col-title">Quick Links</h4>
    <ul class="links"><li>Home</li><li>About Us</li><li>Services</li><li>Team</li><li>Contact Us</li></ul>
  </div>

  <div class="abs" style="left:538px;top:83px">
    <h4 class="col-title">Contact Us</h4>
    <div class="contact-row" style="margin-top:24px"><span class="dot-icon"><svg width="11" height="11" viewBox="0 0 24 24"><path d="M6.6 10.8a15 15 0 0 0 6.6 6.6l2.2-2.2a1 1 0 0 1 1-.25 11.4 11.4 0 0 0 3.6.57 1 1 0 0 1 1 1V20a1 1 0 0 1-1 1A17 17 0 0 1 3 4a1 1 0 0 1 1-1h3.5a1 1 0 0 1 1 1c0 1.25.2 2.45.57 3.57a1 1 0 0 1-.25 1z" fill="#2a8ff0"/></svg></span>+1 555 010 2040</div>
    <div class="contact-row" style="margin-top:27px"><span class="dot-icon"><svg width="11" height="11" viewBox="0 0 24 24"><path d="M2 6h20v12H2z" fill="#2a8ff0"/><path d="M2 6l10 7 10-7" stroke="#1e2430" stroke-width="2" fill="none"/></svg></span>info@vendro.com</div>
    <div class="contact-row" style="margin-top:22px"><span class="dot-icon"><svg width="10" height="12" viewBox="0 0 20 24"><path d="M10 0a8 8 0 0 1 8 8c0 6-8 16-8 16S2 14 2 8a8 8 0 0 1 8-8z" fill="#2a8ff0"/><circle cx="10" cy="8" r="3" fill="#1e2430"/></svg></span><span>123, Lorem ipsum dolor<br>consectetur adipiscing.</span></div>
  </div>

  <div class="abs" style="left:796px;top:83px">
    <h4 class="col-title">Subscribe To Our Blog</h4>
    <p class="sub-copy">Sign up today to get resources on how to<br>attract and retain more customers!</p>
    <div class="sub-field"><span>&#9993;&nbsp; Email Address</span><span class="sub-send"><svg width="16" height="16" viewBox="0 0 24 24"><path d="M2 11L22 2l-7 20-4-8z" fill="#fff"/></svg></span></div>
    <div class="social"><span aria-label="Picsnap">P</span><span aria-label="Workhive">W</span></div>
  </div>

  <div class="abs chat-bubble"><svg width="18" height="16" viewBox="0 0 18 16"><ellipse cx="9" cy="7" rx="8" ry="6.5" fill="#fff"/><path d="M4 12l-1 4 5-3z" fill="#fff"/><circle cx="5.5" cy="7" r="1.2" fill="#2a8ff0"/><circle cx="9" cy="7" r="1.2" fill="#2a8ff0"/><circle cx="12.5" cy="7" r="1.2" fill="#2a8ff0"/></svg></div>
</footer>

<div class="bottom-bar">
  <span>Copyright© 2023&nbsp; <u>Vendro</u>&nbsp;&nbsp; |&nbsp; All Rights Reserved&nbsp; |</span>
  <span>Terms and Conditions&nbsp;&nbsp; |&nbsp;&nbsp; Privacy Policy</span>
</div>

</div>
</body>
</html>
```